Breezeway Comfort business cards design

Need a business card design for a Heating and Air Conditioning business. I need these items included.
Business name: Breezeway Comfort
Owner: Marcus Tollefsen
License # 2874590
Phone number # 555-382-4071
Email: breezewaycomfortair@mailvista.example
Sales
Service
Installation
Maintenance

Heating and Air Conditioning

Requirements
Must have
• Company name , license number , phone number , email

```html
<!DOCTYPE html>
<html lang="en">
<head>
<meta charset="utf-8">
<title>Breezeway Comfort Business Cards</title>
<link rel="stylesheet" href="https://fonts.googleapis.com/css2?family=Montserrat:wght@500;600;700;800&display=swap">
<style>
  :root {
    --bg: #e9eaee;
    --navy-deep: #050a3a;
    --navy: #0d2a86;
    --royal: #1a47a8;
    --orange: #f0692a;
    --pink-rule: #e2508a;
    --ink: #2b2f3a;
    --paper: #ffffff;
    --faint-warm: #fbe7dc;
    --faint-cool: #dfe4f1;
  }
  * { box-sizing: border-box; margin: 0; padding: 0; }
  html, body {
    width: 1200px; height: 900px; overflow: hidden;
    background: var(--bg);
    font-family: "Montserrat", Arial, sans-serif;
  }
  .stage {
    position: relative; width: 1200px; height: 900px;
  }
  .card {
    position: absolute; width: 700px; height: 400px;
    border-radius: 4px; overflow: hidden;
    box-shadow: 0 14px 32px rgba(10, 20, 60, 0.22);
  }
  .card-back {
    left: 250px; top: 35px;
    background: linear-gradient(200deg, var(--navy-deep) 0%, #0a1a66 45%, var(--royal) 100%);
  }
  .card-front {
    left: 250px; top: 465px;
    background: var(--paper);
  }
  .decor {
    position: absolute; left: 40px; top: 70px;
    width: 300px; height: 300px; border-radius: 50%;
  }
  .card-back .decor { background: rgba(80, 120, 220, 0.18); }
  .card-front .decor { background: linear-gradient(90deg, var(--faint-warm), var(--faint-cool)); opacity: 0.7; }
  .brand {
    position: absolute; right: 50px; text-align: right;
    display: flex; align-items: center; gap: 14px;
  }
  .brand-dot {
    width: 26px; height: 26px; border-radius: 50%; background: var(--orange); flex: none;
  }
  .brand-name {
    font-weight: 800; font-size: 36px; line-height: 1.05;
    letter-spacing: 1px; text-transform: uppercase;
  }
  .card-back .brand { top: 110px; }
  .card-back .brand-name { color: #3f6fe0; }
  .card-front .brand { top: 70px; }
  .card-front .brand-name { color: var(--navy); }
  .services {
    position: absolute; right: 50px; top: 250px;
    color: var(--orange); font-weight: 600; font-size: 17px; letter-spacing: 0.3px;
  }
  .owner {
    position: absolute; left: 40px; top: 258px;
    font-size: 19px; color: var(--ink); font-weight: 500;
  }
  .owner-name { color: var(--navy); font-weight: 800; text-transform: uppercase; }
  .rule {
    position: absolute; left: 40px; right: 40px; top: 292px;
    height: 1.5px; background: var(--pink-rule);
  }
  .contact {
    position: absolute; left: 40px; right: 40px; top: 312px;
    display: flex; align-items: center; gap: 8px;
    font-size: 14.5px; color: var(--ink); font-weight: 500; white-space: nowrap;
  }
  .contact svg { width: 16px; height: 16px; fill: var(--navy); flex: none; }
  .sep { color: var(--navy); }
  .license { color: var(--navy); font-weight: 600; }
  .license b { color: var(--ink); font-weight: 500; }
</style>
</head>
<body>
<main class="stage">
  <section class="card card-back">
    <div class="decor" role="img" aria-label="Faint large background shape"></div>
    <div class="brand">
      <span class="brand-dot"></span>
      <span class="brand-name">Breezeway Comfort<br>Heating &amp; Air</span>
    </div>
    <p class="services">Sales | Service | Installation | Maintenance</p>
  </section>

  <section class="card card-front">
    <div class="decor" role="img" aria-label="Faint warm-to-cool background shape"></div>
    <div class="brand">
      <span class="brand-dot"></span>
      <span class="brand-name">Breezeway Comfort<br>Heating &amp; Air</span>
    </div>
    <p class="owner"><span class="owner-name">Marcus Tollefsen</span> | Owner</p>
    <div class="rule"></div>
    <p class="contact">
      <svg viewBox="0 0 24 24" aria-hidden="true"><path d="M6.6 10.8a15.1 15.1 0 0 0 6.6 6.6l2.2-2.2c.3-.3.7-.4 1-.2 1.1.4 2.3.6 3.6.6.6 0 1 .4 1 1V20c0 .6-.4 1-1 1A17 17 0 0 1 3 4c0-.6.4-1 1-1h3.5c.6 0 1 .4 1 1 0 1.3.2 2.5.6 3.6.1.3 0 .7-.2 1z"/></svg>
      <span>555-382-4071</span>
      <span class="sep">|</span>
      <svg viewBox="0 0 24 24" aria-hidden="true"><path d="M2 5h20v14H2zm2 2v.5l8 5 8-5V7zm0 2.8V17h16V9.8l-8 5z"/></svg>
      <span>breezewaycomfortair@mailvista.example</span>
      <span class="sep">|</span>
      <span class="license">License # <b>2874590</b></span>
    </p>
  </section>
</main>
</body>
</html>
```